Website design that will showcase a medical assistance tool

I want the medical assistance tool (for hearing aids) website to have a premium or upmarket feel. The brand is Plivoran (as per attached logo image for guidance). I want the website to appeal to both end users as well as hearing aid clinics.

```html
<!DOCTYPE html>
<html lang="en">
<head>
<meta charset="utf-8">
<title>Plivoran — Precision. Comfort. Care.</title>
<link href="https://fonts.googleapis.com/css2?family=Montserrat:wght@400;500;600&family=Roboto:wght@400;500;700&display=swap" rel="stylesheet">
<style>
:root{
  --sand:#c9c3ae;
  --sand-light:#d6d1bf;
  --slate:#646464;
  --ink:#222;
  --text:#555;
  --white:#fff;
  --star:#f2b01e;
}
*{margin:0;padding:0;box-sizing:border-box}
html,body{width:1200px;height:3587px;overflow:hidden}
body{position:relative;background:var(--white);font-family:"Roboto",sans-serif;color:var(--text)}
.abs{position:absolute}
.heading{font-family:"Montserrat",sans-serif;font-weight:500}
.btn{position:absolute;display:flex;align-items:center;justify-content:center;gap:8px;background:var(--sand);color:var(--white);font-weight:700;border-radius:30px;font-size:15px;letter-spacing:.3px}
.btn .dot{width:14px;height:14px;border-radius:50%;background:var(--white);position:relative}
.btn .dot::after{content:"";position:absolute;left:4px;top:3.5px;border-left:6px solid var(--sand);border-top:3.5px solid transparent;border-bottom:3.5px solid transparent}

/* header */
.site-header{position:absolute;left:0;top:0;width:1200px;height:107px;background:var(--white)}
.brand{position:absolute;left:110px;top:56px;display:flex;align-items:center;gap:10px;font-family:"Montserrat",sans-serif;font-size:34px;color:var(--slate);font-weight:400}
.brand .mark{width:30px;height:30px;border-radius:50%;background:var(--sand)}
.topbar{position:absolute;left:668px;top:0;width:418px;height:31px}
.nav{position:absolute;top:60px;font-size:15px;color:var(--ink);font-weight:500}
.nav.active{color:var(--sand)}

/* hero */
.hero{position:absolute;left:0;top:107px;width:1200px;height:581px;background:linear-gradient(100deg,#6b5a48 0%,#9a8672 30%,#c9b9a6 55%,#a58c78 80%,#6a5447 100%)}
.hero-title{position:absolute;left:110px;top:256px;font-size:45px;line-height:51px;color:var(--white);font-weight:500}
.hero-sub{position:absolute;left:111px;top:380px;width:430px;font-size:17px;line-height:27px;color:var(--white);font-weight:500}
.arrow{position:absolute;width:44px;height:44px;border:2px solid var(--white);border-radius:50%}

/* how it works */
.how{position:absolute;left:0;top:688px;width:1200px;height:470px;background:var(--sand)}
.section-title{position:absolute;left:0;width:1200px;text-align:center;font-size:42px}
.step-art{position:absolute;top:157px;width:186px;height:140px;border-radius:70px;background:var(--sand-light)}
.step{position:absolute;width:320px;text-align:center;color:var(--white)}
.step h3{font-size:18px;font-weight:500;margin-bottom:12px}
.step p{font-size:14px;line-height:24px}

/* about */
.about-title{position:absolute;left:113px;top:1300px;font-size:46px;color:var(--ink)}
.about-text{position:absolute;left:113px;top:1374px;width:436px;font-size:14px;line-height:25.6px;text-align:justify;color:var(--text)}
.about-text p{margin-bottom:12px}

/* features */
.feat-title{position:absolute;left:654px;top:1894px;font-size:44px;line-height:51px;color:var(--white)}
.feat-sub{position:absolute;left:654px;top:2004px;width:440px;font-size:15px;line-height:24px;color:var(--white);font-weight:500}
.feat-item{position:absolute;left:654px;display:flex;gap:22px;align-items:center;color:var(--white)}
.feat-item .ico{width:68px;height:68px;border-radius:50%;background:var(--sand);flex:none}
.feat-item h4{font-size:17px;font-weight:500;margin-bottom:8px}
.feat-item p{font-size:14px}

/* testimonials */
.card{position:absolute;top:2566px;width:314px;height:216px;background:var(--white);border-radius:6px;box-shadow:0 3px 10px rgba(0,0,0,.1);border-bottom:3px solid var(--sand);padding:24px 26px}
.stars{color:var(--star);font-size:16px;letter-spacing:2px}
.card p{margin-top:8px;font-size:13.5px;line-height:22.4px;text-align:justify;color:var(--text)}
.person{display:flex;align-items:center;gap:12px;margin-top:14px}
.person .avatar{width:46px;height:46px;border-radius:50%;background:linear-gradient(#9aa3ad,#5f6b78)}
.person b{display:block;font-size:16px;font-weight:500;color:var(--ink)}
.person small{font-size:12px;color:#888}

/* promises */
.promise{position:absolute;display:flex;gap:20px;align-items:center;color:var(--white)}
.promise .ico{width:78px;height:78px;border-radius:50%;background:var(--white);flex:none}
.promise h4{font-size:18px;font-weight:500;margin-bottom:6px}
.promise p{font-size:14px;line-height:22px}

/* footer */
.footer{position:absolute;left:0;top:3116px;width:1200px;height:471px}
.sub-title{position:absolute;left:135px;top:3208px;font-size:35px;color:var(--white);font-family:"Montserrat",sans-serif;font-weight:400}
.sub-input{position:absolute;left:532px;top:3211px;width:370px;height:42px;border-radius:22px;background:var(--white);border:1px solid var(--sand);font-size:12px;color:#777;padding:14px 22px}
.sub-btn{position:absolute;left:920px;top:3212px;width:144px;height:42px;border-radius:22px;background:var(--sand);color:var(--white);font-size:15px;font-weight:500;display:flex;align-items:center;justify-content:center}
.fcol{position:absolute;top:3334px;color:var(--white)}
.fcol h5{font-size:16px;font-weight:500;margin-bottom:14px}
.fcol li{list-style:none;font-size:12px;line-height:22.4px}
.fcol .row{display:flex;align-items:flex-start;gap:12px;font-size:12px;line-height:15px;margin-bottom:14px}
.fcol .ic{width:11px;height:11px;flex:none;margin-top:2px;background:var(--white);border-radius:2px}
.social{display:flex;align-items:center;gap:12px;font-size:12px;margin-bottom:6px}
.social i{width:28px;height:28px;border-radius:50%;background:var(--sand);display:block}
.vline{position:absolute;top:3336px;width:1px;height:148px;background:#777}
.copy{position:absolute;left:0;top:3550px;width:1200px;text-align:center;font-size:11px;color:var(--white)}
</style>
</head>
<body>

<header class="site-header">
  <div class="brand"><span class="mark"></span>Plivoran</div>
  <svg class="topbar" viewBox="0 0 418 31" width="418" height="31">
    <polygon points="0,0 190,0 190,31 22,31" fill="var(--sand)"/>
    <polygon points="190,0 418,0 396,31 190,31" fill="var(--slate)"/>
  </svg>
  <span class="abs" style="left:703px;top:8px;font-size:14px;color:#fff;font-weight:500">&#9990; +1 888 888 8888</span>
  <span class="abs" style="left:868px;top:8px;font-size:14px;color:#fff;font-weight:500">&#9993; support@plivoran.com</span>
  <span class="nav active" style="left:405px">Home</span>
  <span class="nav" style="left:474px">About</span>
  <span class="nav" style="left:542px">Features</span>
  <span class="nav" style="left:629px">How It Works</span>
  <span class="nav" style="left:748px">For Clinics</span>
  <span class="nav" style="left:848px">Contact</span>
  <div class="btn" style="left:935px;top:49px;width:152px;height:42px;font-weight:500;font-size:15px">Shop Now</div>
</header>

<section class="hero" role="img" aria-label="Photo of an older woman having a hearing aid fitted behind her ear"></section>
<svg class="abs" style="left:0;top:107px" width="1200" height="582" viewBox="0 0 1200 582">
  <path d="M1200 360 C1190 490 1110 560 960 581 L1200 581 Z" fill="var(--sand)"/>
</svg>
<h1 class="hero-title heading">Precision. Comfort.<br>Care.</h1>
<p class="hero-sub">The premium tool designed for safe, effective hearing aid maintenance.</p>
<div class="btn" style="left:111px;top:461px;width:204px;height:54px">GET STARTED <span class="dot"></span></div>
<div class="arrow" style="left:31px;top:378px"><svg width="40" height="40" viewBox="0 0 40 40"><path d="M23 12 L15 20 L23 28" stroke="#fff" stroke-width="2.5" fill="none"/></svg></div>
<div class="arrow" style="left:1124px;top:378px"><svg width="40" height="40" viewBox="0 0 40 40"><path d="M17 12 L25 20 L17 28" stroke="#fff" stroke-width="2.5" fill="none"/></svg></div>

<section class="how">
  <h2 class="section-title heading" style="top:68px;color:#fff">How It Works</h2>
  <div class="step-art" style="left:160px" role="img" aria-label="Illustration of the number one beside a checklist icon"></div>
  <div class="step-art" style="left:497px" role="img" aria-label="Illustration of the number two beside an adjustment sliders icon"></div>
  <div class="step-art" style="left:837px" role="img" aria-label="Illustration of the number three beside a protective shield icon"></div>
  <div class="step" style="left:96px;top:320px"><h3>Prepare</h3><p>Hold your hearing aid securely in a well-lit<br>space.</p></div>
  <div class="step" style="left:439px;top:320px"><h3>Clean &amp; Adjust</h3><p>Use Plivoran for safe wax removal or<br>precise adjustments.</p></div>
  <div class="step" style="left:780px;top:320px"><h3>Store Safely</h3><p>Place Plivoran in its protective case to keep it<br>sterile and ready.</p></div>
</section>

<svg class="abs" style="left:0;top:1158px" width="1200" height="688" viewBox="0 0 1200 688">
  <rect width="1200" height="688" fill="var(--slate)"/>
  <path d="M150 0 H1200 V520 C1200 620 1100 688 960 688 H0 V140 C0 60 60 0 150 0 Z" fill="#fff"/>
  <path d="M0 0 H150 C60 0 0 60 0 140 Z" fill="var(--sand)"/>
</svg>
<h2 class="about-title heading">About Us</h2>
<div class="about-text">
  <p>At Plivoran, our mission is to improve hearing aid maintenance for everyone — from experienced audiologists to first-time hearing aid users. We designed Plivoran alongside hearing care professionals to meet the highest standards of safety, accuracy, and comfort.</p>
  <p>Lorem ipsum dolor sit amet, consectetur adipiscing elit, sed do eiusmod tempor incididunt ut labore et dolore magna aliqua. Ut enim ad minim veniam, quis nostrud exercitation ullamco laboris nisi ut aliquip ex ea commodo consequat.</p>
</div>
<div class="btn" style="left:113px;top:1620px;width:164px;height:42px;font-size:14px">READ MORE <span class="dot"></span></div>
<div class="abs" style="left:631px;top:1257px;width:214px;height:191px;background:var(--slate);border-radius:26px 0 0 0"></div>
<div class="abs" style="left:892px;top:1524px;width:215px;height:188px;background:var(--sand);border-radius:0 0 26px 0"></div>
<div class="abs" role="img" aria-label="Photo of a smiling woman placing a hearing aid in her ear" style="left:650px;top:1275px;width:437px;height:421px;background:linear-gradient(135deg,#b7b3a6,#8e8a6e 55%,#6f7248)"></div>

<svg class="abs" style="left:0;top:1845px" width="1200" height="560" viewBox="0 0 1200 560">
  <rect width="1200" height="560" fill="var(--slate)"/>
  <defs>
    <linearGradient id="handGrad" x1="0" y1="0" x2="1" y2="1">
      <stop offset="0" stop-color="#d9b48e"/><stop offset=".5" stop-color="#e7cdc4"/><stop offset="1" stop-color="#c99f86"/>
    </linearGradient>
  </defs>
  <path d="M0 0 H565 C620 90 610 420 430 520 C380 548 330 560 270 560 H0 Z" fill="var(--sand)"/>
  <path d="M0 0 H548 C600 90 590 410 415 510 C370 540 320 552 260 552 H0 Z" fill="#fff"/>
  <path d="M0 0 H535 C585 90 575 400 405 500 C360 528 315 540 255 540 H0 Z" fill="url(#handGrad)" role="img" aria-label="Photo of hands holding a charging case with two hearing aids"/>
</svg>
<h2 class="feat-title heading">Engineered for<br>Safety &amp; Precision</h2>
<p class="feat-sub">Every detail of Plivoran is crafted with care and backed by professional insight.</p>
<div class="feat-item" style="top:2092px"><span class="ico"></span><div><h4>Ergonomic Design</h4><p>Non-slip grip for steady, confident handling.</p></div></div>
<div class="feat-item" style="top:2186px"><span class="ico"></span><div><h4>Medical-Grade Materials</h4><p>Built for durability and hygiene.</p></div></div>
<div class="feat-item" style="top:2280px"><span class="ico"></span><div><h4>Clinically Tested</h4><p>Developed with hearing care specialists.</p></div></div>

<svg class="abs" style="left:0;top:2404px" width="1200" height="712" viewBox="0 0 1200 712">
  <rect width="1200" height="712" fill="var(--sand)"/>
  <path d="M0 0 H1200 V330 C1200 420 1120 503 1000 503 H0 Z" fill="#fff"/>
</svg>
<h2 class="section-title heading" style="top:2475px;color:var(--slate)">Hear From Our Users</h2>
<div class="card" style="left:111px"><div class="stars">★★★★★</div><p>“ Lorem ipsum dolor sit amet, consectetur adipiscing elit, sed do eiusmod tempor incididunt ut labore et dolore magna aliqua. Ut enim ad minim veniam ”</p><div class="person"><span class="avatar"></span><div><b>John Doe</b><small>USA</small></div></div></div>
<div class="card" style="left:443px"><div class="stars">★★★★★</div><p>“ Lorem ipsum dolor sit amet, consectetur adipiscing elit, sed do eiusmod tempor incididunt ut labore et dolore magna aliqua. Ut enim ad minim veniam ”</p><div class="person"><span class="avatar"></span><div><b>John Doe</b><small>USA</small></div></div></div>
<div class="card" style="left:774px"><div class="stars">★★★★★</div><p>“ Lorem ipsum dolor sit amet, consectetur adipiscing elit, sed do eiusmod tempor incididunt ut labore et dolore magna aliqua. Ut enim ad minim veniam ”</p><div class="person"><span class="avatar"></span><div><b>John Doe</b><small>USA</small></div></div></div>

<div class="promise" style="left:113px;top:2972px"><span class="ico"></span><div><h4>Satisfaction</h4><p>Authentic Products at Competitive<br>Prices</p></div></div>
<div class="promise" style="left:503px;top:2972px"><span class="ico"></span><div><h4>Safety</h4><p>Authorized Distributor of<br>Dunmore &amp; Vale</p></div></div>
<div class="promise" style="left:837px;top:2972px"><span class="ico"></span><div><h4>Support</h4><p>Support Available 24/7</p></div></div>

<svg class="footer" viewBox="0 0 1200 471" width="1200" height="471">
  <rect width="1200" height="471" fill="var(--sand)"/>
  <path d="M150 0 H1200 V471 H0 V150 C0 60 60 0 150 0 Z" fill="var(--slate)"/>
  <rect x="113" y="183" width="975" height="1" fill="#7a7a7a"/>
  <rect x="113" y="406" width="975" height="1" fill="#7a7a7a"/>
</svg>
<h2 class="sub-title">Subscribe Newsletter</h2>
<div class="sub-input">Enter Your Email Address</div>
<div class="sub-btn">SUBSCRIBE</div>

<div class="fcol" style="left:113px"><h5>QUICK LINKS</h5><ul><li>Home</li><li>About</li><li>Products</li><li>Shop now</li><li>Sign in</li></ul></div>
<div class="vline" style="left:270px"></div>
<div class="fcol" style="left:349px"><h5>INFORMATION</h5><ul><li>Terms &amp; Conditions</li><li>Privacy Policy</li><li>Disclaimer</li><li>Site Map</li><li>Contact Us</li><li>Categories</li></ul></div>
<div class="vline" style="left:536px"></div>
<div class="fcol" style="left:614px"><h5>CONTACT INFO</h5>
  <div class="row"><span class="ic"></span>(888) 888-8888</div>
  <div class="row"><span class="ic"></span>(123) 456-7890</div>
  <div class="row"><span class="ic"></span><u>info@plivoran.com</u></div>
  <div class="row"><span class="ic" style="border-radius:50% 50% 50% 0"></span>#2868 Lorem ipsum dolor sit<br>amet, consectetur</div>
</div>
<div class="vline" style="left:874px"></div>
<div class="fcol" style="left:952px"><h5>FOLLOW US</h5>
  <div class="social"><i></i>Circlebook</div>
  <div class="social"><i></i>Chirper</div>
  <div class="social"><i></i>Glimmer Plus</div>
  <div class="social"><i></i>Linkwork</div>
</div>
<p class="copy">Copyrights © The Company name 2025 | Allrights Reserved</p>

</body>
</html>
```